Stylish new business card needed!

Hello everyone! I am in need of a new business card design for an alarm company here in Hurricane WV. I have all fonts, color codes and logos provided for you use! We are a young company and like the style of a clean sleek looking business card. Would like it double sided, one side holding the logo and the other with your design!
Target Market(s)
The people that are looking for the newest tech for home automation and security
Industry/Entity Type
Alarm services; Home automation
Contact Information for Business Card
Name of person; position (Sales; Installer); Phone Number (555.418.7290); Employee cell Number; Website (www.GuardedByVemlo.example); Employee Email; Double sided
Look and feel
Each slider illustrates characteristics of the customer's brand and the style your logo design should communicate.

```html
<!DOCTYPE html>
<html lang="en">
<head>
<meta charset="utf-8">
<title>Guarded By Vemlo – Business Card</title>
<link href="https://fonts.googleapis.com/css2?family=Arimo:wght@400;700&display=swap" rel="stylesheet">
<style>
  :root {
    --backdrop: #232323;
    --card: #1f1f23;
    --emboss: #0f0f11;
    --accent: #f08a3c;
    --text-light: #ffffff;
    --text-grey: #9a9a9e;
  }
  * { box-sizing: border-box; margin: 0; padding: 0; }
  html, body {
    width: 1200px; height: 780px; overflow: hidden;
    background: var(--backdrop);
    font-family: "Arimo", Arial, sans-serif;
  }
  .sheet {
    width: 1200px; height: 780px;
    display: flex; align-items: center; justify-content: center; gap: 40px;
  }
  .card {
    position: relative;
    width: 540px; height: 310px;
    background: var(--card);
    border-bottom: 5px solid var(--accent);
    box-shadow: 0 10px 28px rgba(0,0,0,.55);
    overflow: hidden;
  }

  /* Front: brand side */
  .card--front { display: flex; align-items: center; justify-content: center; }
  .brand { text-align: center; color: var(--emboss); font-weight: 700; }
  .brand__name { display: flex; align-items: center; gap: 14px; font-size: 62px; letter-spacing: 1px; line-height: 1; }
  .brand__mark { width: 22px; height: 22px; border-radius: 50%; background: var(--emboss); }
  .brand__tagline { margin-top: 14px; font-size: 12px; letter-spacing: 1.5px; text-transform: uppercase; }

  /* Back: contact side */
  .card--back { display: flex; align-items: center; padding: 0 34px 0 44px; }
  .person { flex: 0 0 auto; font-weight: 700; text-align: right; padding-right: 26px; }
  .person__name { font-size: 27px; line-height: 1.1; }
  .person__first { color: var(--accent); }
  .person__last { color: var(--text-grey); }
  .person__role { font-size: 14px; color: var(--text-light); margin-top: 4px; }
  .divider { width: 2px; height: 84px; background: var(--text-light); flex: 0 0 auto; }
  .contacts { list-style: none; padding-left: 22px; font-size: 13px; color: var(--text-light); }
  .contacts li { display: flex; align-items: center; gap: 10px; line-height: 1.75; white-space: nowrap; }
  .contacts svg { width: 14px; height: 14px; flex: 0 0 auto; fill: none; stroke: var(--accent); stroke-width: 2; }
</style>
</head>
<body>
<main class="sheet">

  <section class="card card--front" aria-label="Card front">
    <div class="brand">
      <div class="brand__name"><span class="brand__mark"></span>GUARDED BY VEMLO</div>
      <div class="brand__tagline">Automation and Security Services</div>
    </div>
  </section>

  <section class="card card--back" aria-label="Card back">
    <div class="person">
      <div class="person__name"><span class="person__first">Mira</span> <span class="person__last">Kovanek</span></div>
      <div class="person__role">Sales; Installer</div>
    </div>
    <div class="divider"></div>
    <ul class="contacts">
      <li>
        <svg viewBox="0 0 24 24" aria-hidden="true"><path d="M5 3h4l2 5-3 2a12 12 0 0 0 6 6l2-3 5 2v4a2 2 0 0 1-2 2A18 18 0 0 1 3 5a2 2 0 0 1 2-2z"/></svg>
        555.418.7290
      </li>
      <li>
        <svg viewBox="0 0 24 24" aria-hidden="true"><rect x="6" y="2" width="12" height="20" rx="2"/><line x1="11" y1="18" x2="13" y2="18"/></svg>
        555.418.7311
      </li>
      <li>
        <svg viewBox="0 0 24 24" aria-hidden="true"><circle cx="12" cy="12" r="10"/><path d="M2 12h20M12 2a15 15 0 0 1 0 20M12 2a15 15 0 0 0 0 20"/></svg>
        www.GuardedByVemlo.example
      </li>
      <li>
        <svg viewBox="0 0 24 24" aria-hidden="true"><rect x="2" y="5" width="20" height="14" rx="1"/><path d="M2 6l10 7 10-7"/></svg>
        info@GuardedByVemlo.example
      </li>
    </ul>
  </section>

</main>
</body>
</html>
```